Dusk n Shine - Contact/Landing Page

I need a landing page which will essentially be the page that customers will go to from the 'website' link on ZVX listing. It will provide a short overview of services which need to be selectable. a little further down can capture some contact details followed by a large Submit Now button etc...

I have some icon/logo's that can be utilised at the bottom of the page as industry type references.

End of Lease Cleaning Services

Cleaning Service

• As per description
• Colours to match my website dusknshine.com.au

```html
<!DOCTYPE html>
<html lang="en">
<head>
<meta charset="utf-8">
<title>Dusk n Shine – End of Lease Cleaning</title>
<link href="https://fonts.googleapis.com/css2?family=Roboto:wght@300;400;500;700&display=swap" rel="stylesheet">
<style>
  :root{
    --brand-blue:#1e9ad6;
    --panel-blue:#22b9e2;
    --ink:#222833;
    --footer:#212733;
    --grey-text:#6b7076;
    --icon-grey:#b9b9b9;
    --field-text:#8a8f95;
    --white:#ffffff;
  }
  *{box-sizing:border-box;margin:0;padding:0}
  html,body{width:833px;height:1200px;overflow:hidden;background:var(--white)}
  body{position:relative;font-family:'Roboto',sans-serif;color:var(--ink)}
  .abs{position:absolute}

  /* Hero */
  .hero{left:0;top:0;width:833px;height:372px;overflow:hidden}
  .hero-scene{left:0;top:0;width:833px;height:372px;
    background:
      radial-gradient(ellipse 180px 110px at 78% 12%,rgba(236,226,200,.9) 0%,rgba(236,226,200,0) 100%),
      radial-gradient(ellipse 120px 60px at 70% 75%,rgba(120,86,50,.75) 0%,rgba(120,86,50,0) 100%),
      linear-gradient(180deg,#6e6b66 0%,#8d8a84 28%,#a8a9a6 45%,#bfc8cb 65%,#aab7bd 100%)}
  .hero-wave{left:0;top:332px;width:833px;height:40px}
  .logo-box{left:362px;top:16px;width:102px;height:125px;background:var(--white);
    display:flex;align-items:center;justify-content:center;flex-direction:column;gap:8px}
  .logo-mark{width:16px;height:16px;background:var(--brand-blue)}
  .logo-name{font-weight:700;color:var(--brand-blue);font-size:14px;text-align:center;line-height:1.1}
  .hero-title{left:0;top:157px;width:833px;text-align:center;color:var(--white);
    font-size:23px;font-weight:500;white-space:pre;line-height:28px}

  /* Services */
  .service{top:412px;width:214px;text-align:center}
  .service-icon{display:block;width:68px;height:68px;margin:0 auto}
  .service-title{margin-top:14px;font-size:19px;line-height:24px;font-weight:400;color:var(--brand-blue)}
  .service-desc{margin-top:9px;font-size:9.6px;line-height:15.7px;color:var(--grey-text);font-weight:400}
  .select-btn{margin:8px auto 0;width:94px;height:31px;border-radius:16px;background:var(--ink);
    color:var(--white);font-size:12.5px;display:flex;align-items:center;justify-content:center;gap:8px}
  .check{width:9px;height:9px;background:var(--white);border-radius:2px;display:block}

  /* Contact */
  .contact{left:0;top:651px;width:833px;height:302px;
    background:
      radial-gradient(ellipse 70px 130px at 6% 55%,rgba(235,235,235,.95) 0%,rgba(235,235,235,0) 100%),
      linear-gradient(90deg,#c9c7c4 0%,#a7a19a 18%,#8a7f75 38%,#6e6157 52%,#9c948b 68%,#b9b4ad 82%,#7b7f85 100%)}
  .field{left:120px;width:281px;height:38px;background:var(--white);
    font-size:10px;color:var(--field-text);padding-left:15px;display:flex;align-items:center}
  .contact-panel{left:432px;top:689px;width:281px;height:226px;background:var(--panel-blue)}
  .panel-brand{left:0;top:20px;width:281px;display:flex;flex-direction:column;align-items:center;gap:10px}
  .panel-mark{width:22px;height:22px;background:var(--white)}
  .panel-name{font-size:24px;line-height:28px;font-weight:700;color:var(--white)}
  .panel-mail{left:0;top:126px;width:281px;display:flex;align-items:center;justify-content:center;gap:12px;
    color:var(--white);font-size:16.5px;line-height:20px}
  .submit-btn{left:40px;top:154px;width:201px;height:59px;background:var(--ink);color:var(--white);
    font-size:35px;font-weight:500;display:flex;align-items:center;justify-content:center}

  /* Accreditations */
  .badge{top:996px;height:43px;border-radius:3px}
  .badge-dark{left:120px;width:103px;background:linear-gradient(90deg,#f4f4f4 0 40%,#1b1b1b 40% 100%);border:1px solid #1b1b1b}
  .badge-flag{left:266px;width:155px;background:linear-gradient(90deg,#3b3f8f 0%,#e5e8f0 40%,#f3f3f3 100%);border-radius:0}
  .badge-navy{left:462px;width:72px;background:linear-gradient(90deg,#1c3f8a 0 68%,#e04646 68% 100%);border-radius:0}
  .badge-green{left:570px;width:143px;background:#8cbf3a;border-radius:0}

  /* Footer */
  .footer{left:0;top:1070px;width:833px;height:130px}
  .epa-badge{left:120px;top:1133px;width:82px;height:28px;border:1.5px solid #e8eaed;border-radius:14px}
  .licence{left:120px;top:1165px;color:var(--white);font-size:8px;line-height:10px}
  .copyright{left:0;top:1148px;width:833px;text-align:center;color:var(--white);font-size:8.4px;line-height:10px}
  .social{left:672px;top:1131px;width:41px;height:41px;background:#3b5bb0}
</style>
</head>
<body>

  <header class="abs hero">
    <div class="abs hero-scene" role="img" aria-label="Blurred photo of a cockroach lying on its back on a wooden floor"></div>
    <svg class="abs hero-wave" viewBox="0 0 833 40" preserveAspectRatio="none">
      <path d="M0 38 Q416 -12 833 38 L833 40 L0 40 Z" fill="var(--brand-blue)"/>
      <path d="M0 40 Q416 3 833 40 Z" fill="var(--white)"/>
    </svg>
    <div class="abs logo-box">
      <span class="logo-mark"></span>
      <span class="logo-name">Dusk n Shine</span>
    </div>
    <h1 class="abs hero-title">END OF LEASE CLEANING   |   LICENSED PEST CONTROL</h1>
  </header>

  <section class="abs service" style="left:96px">
    <svg class="service-icon" viewBox="0 0 68 68" fill="none" stroke="var(--icon-grey)" stroke-width="2" role="img" aria-label="Floor plan icon">
      <rect x="2" y="2" width="64" height="64"/>
      <rect x="6" y="6" width="56" height="56"/>
      <path d="M6 30 H26 M34 30 H62 M26 6 V22 M40 6 V18 M40 30 V44 M20 44 V62 M48 44 V62 M26 44 H48"/>
      <rect x="10" y="10" width="12" height="14"/>
      <rect x="44" y="10" width="14" height="8"/>
      <circle cx="34" cy="56" r="3"/>
    </svg>
    <h2 class="service-title">Cleaning</h2>
    <p class="service-desc">All interior cleaning carried out to<br>Property management requirements.</p>
    <div class="select-btn">Select
      <svg width="9" height="9" viewBox="0 0 9 9"><rect width="9" height="9" rx="2" fill="#2f9be0"/><path d="M2 4.6 L3.8 6.3 L7 2.8" stroke="#fff" stroke-width="1.4" fill="none"/></svg>
    </div>
  </section>

  <section class="abs service" style="left:310px">
    <svg class="service-icon" viewBox="0 0 68 68" fill="none" stroke="var(--icon-grey)" stroke-width="2" role="img" aria-label="Carpet roll icon">
      <path d="M2 8 H52 M2 66 H58 M2 8 V66"/>
      <path d="M6 8 V66" stroke-dasharray="1.5 2"/>
      <rect x="12" y="16" width="34" height="42"/>
      <rect x="18" y="22" width="22" height="30"/>
      <path d="M24 30 H34 V44 H24 Z"/>
      <path d="M52 8 A7 7 0 0 1 66 8 V58"/>
      <circle cx="59" cy="58" r="8"/>
      <circle cx="59" cy="58" r="4"/>
    </svg>
    <h2 class="service-title">Carpet Cleaning</h2>
    <p class="service-desc">Carpet stain cleaning to Australian<br>standard AS 3733 : 1995</p>
    <div class="select-btn">Select <span class="check"></span></div>
  </section>

  <section class="abs service" style="left:523px">
    <svg class="service-icon" viewBox="0 0 68 68" fill="none" stroke="var(--icon-grey)" stroke-width="2.4" role="img" aria-label="No-pests icon">
      <circle cx="34" cy="34" r="30"/>
      <path d="M13 55 L55 13"/>
      <ellipse cx="34" cy="38" rx="10" ry="14"/>
      <circle cx="34" cy="20" r="5"/>
    </svg>
    <h2 class="service-title">Pest Control</h2>
    <p class="service-desc">Mandatory requirement for pets<br>on-premises</p>
    <div class="select-btn">Select <span class="check"></span></div>
  </section>

  <section class="abs contact" role="img" aria-label="Photo of a pest control technician with a sprayer in a living room"></section>
  <div class="abs field" style="top:689px">First Name</div>
  <div class="abs field" style="top:736px">Surname</div>
  <div class="abs field" style="top:783px">Email</div>
  <div class="abs field" style="top:830px">Phone</div>
  <div class="abs field" style="top:877px">Suburb</div>

  <aside class="abs contact-panel">
    <div class="abs panel-brand">
      <span class="panel-mark"></span>
      <span class="panel-name">Dusk n Shine</span>
    </div>
    <div class="abs panel-mail">
      <svg width="18" height="13" viewBox="0 0 18 13"><rect x="0.7" y="0.7" width="16.6" height="11.6" fill="none" stroke="#fff" stroke-width="1.4"/><path d="M1 1 L9 7.5 L17 1 M1 12 L7 6 M17 12 L11 6" stroke="#fff" stroke-width="1.4" fill="none"/></svg>
      <span>info@dusknshine.com.au</span>
    </div>
    <div class="abs submit-btn">SUBMIT</div>
  </aside>

  <div class="abs badge badge-dark" role="img" aria-label="Carpet cleaning certification badge"></div>
  <div class="abs badge badge-flag" role="img" aria-label="Decontamination systems partner badge"></div>
  <div class="abs badge badge-navy" role="img" aria-label="Training institute badge"></div>
  <div class="abs badge badge-green" role="img" aria-label="Environmental studies college badge"></div>

  <svg class="abs footer" viewBox="0 0 833 130" preserveAspectRatio="none">
    <path d="M0 35 Q416 -5 833 35 L833 130 L0 130 Z" fill="var(--brand-blue)"/>
    <path d="M0 35 Q416 12 833 35 L833 130 L0 130 Z" fill="var(--footer)"/>
  </svg>
  <div class="abs epa-badge" role="img" aria-label="Environment authority badge"></div>
  <p class="abs licence">Pest Licence : 5031846</p>
  <p class="abs copyright">© Copyright 2021 Company Name. All Rights Reserved.</p>
  <div class="abs social" role="img" aria-label="Social media link"></div>

</body>
</html>
```